Welding Fabrication and Inspection Business Card Design

Welding Fabrication and Inspection Services,

Business

Industrial Machinery ServicesMohammed Rahim30 Ballarat Street, Mount Gravatt East.4122.QLD

```html
<!DOCTYPE html>
<html lang="en">
<head>
<meta charset="utf-8">
<title>Tarnwell Forge Services – Business Cards</title>
<link rel="stylesheet" href="https://fonts.googleapis.com/css2?family=Barlow:wght@400;600;700&family=Barlow+Semi+Condensed:wght@500&family=Roboto:wght@400&display=swap">
<style>
  :root {
    --backdrop: #a19e9f;
    --card: #fbfbfb;
    --ink: #231f20;
    --band: #2a2526;
    --on-band: #ffffff;
    --tool-red: #8e2a30;
    --tool-dark: #3a3536;
  }
  * { margin: 0; padding: 0; box-sizing: border-box; }
  html, body { width: 1200px; height: 1200px; overflow: hidden; }
  body { background: var(--backdrop); position: relative; font-family: "Barlow", sans-serif; color: var(--ink); }

  .card { position: absolute; width: 713px; height: 418px; background: var(--card); overflow: hidden; }
  .card--front { left: 238px; top: 119px; }
  .card--back { left: 230px; top: 643px; }

  .front-brand {
    position: absolute; left: 0; right: 0; top: 160px;
    text-align: center; font-weight: 700; font-size: 40px; color: var(--ink);
  }
  .front-band {
    position: absolute; left: 0; right: 0; bottom: 0; height: 70px;
    background: var(--band); color: var(--on-band);
    display: flex; align-items: center; justify-content: center;
    font-weight: 600; font-size: 23px; letter-spacing: 0.2px;
  }

  .back-wave { position: absolute; left: 0; top: 0; width: 713px; height: 200px; }
  .back-tagline {
    position: absolute; right: 22px; top: 30px; text-align: right;
    font-family: "Barlow Semi Condensed", sans-serif; font-weight: 500;
    font-size: 21px; line-height: 29px; color: var(--on-band);
  }
  .back-brand {
    position: absolute; left: 40px; top: 178px;
    font-weight: 700; font-size: 30px; color: var(--ink);
  }
  .contact { position: absolute; left: 41px; top: 258px; }
  .contact__name { font-weight: 700; font-size: 29px; line-height: 36px; }
  .contact__role { font-weight: 600; font-size: 17px; margin-top: 2px; }
  .contact__address { font-family: "Roboto", sans-serif; font-size: 17px; line-height: 25px; margin-top: 18px; }

  .tool-photo {
    position: absolute; left: 488px; top: 248px; width: 212px; height: 150px;
    background: linear-gradient(180deg, var(--tool-red) 0%, var(--tool-red) 40%, var(--tool-dark) 100%);
    border-radius: 6px;
  }
</style>
</head>
<body>

  <section class="card card--front">
    <div class="front-brand">Tarnwell Forge Services</div>
    <div class="front-band">Welding Fabrication and Inspection Services</div>
  </section>

  <section class="card card--back">
    <svg class="back-wave" viewBox="0 0 713 200" aria-hidden="true">
      <path d="M0,0 H713 V178 C610,172 520,135 420,98 C320,62 150,45 0,78 Z" fill="var(--band)"/>
      <path d="M0,52 C150,14 330,34 432,76 C535,118 625,152 713,160" fill="none" stroke="var(--card)" stroke-width="7"/>
    </svg>
    <div class="back-tagline">Welding Fabrication and<br>Inspection Services</div>
    <div class="back-brand">Tarnwell Forge Services</div>
    <div class="contact">
      <div class="contact__name">Khalid Nasser</div>
      <div class="contact__role">Owner</div>
      <div class="contact__address">17 Corrowen Street, Kelverton Heights<br>4187. QLD</div>
    </div>
    <div class="tool-photo" role="img" aria-label="Photo of a red magnetic particle inspection yoke with hinged legs"></div>
  </section>

</body>
</html>
```